Natural Skincare Product Labels Design

We are looking for a designer to create elegant but quirky, functional product labels for our natural skincare range.
The labels must reflect our brand’s values of simplicity, luxury, and the natural, handmade essence of our products.
https://www.pictogrove.com/marvellaskincare
1. Key Details
Packaging Dimensions
Container Types: Transparent jars.
Sizes for Body Products:
Diameter: 64mm–68mm.
Heights: 80mm, 88mm, and 97mm (lid height: 15mm).
Sizes for Face Creams:
Diameter: 60mm.
Height: 50mm (lid height: 15mm).
Label Fit: For body products, ideally one label size to fit all jar sizes.
For the smaller face cream jars, a separate, tailored label is required.
2. Label Placement
Options include a wrapped-around label or a combination of wrapped-around and top-of-jar elements.
Transparent jars mean the label must leave space for the product to be visible (e.g., partial wrap or cutout areas).
3. Content Requirements
Product Name: Prominently displayed.
Ingredient List: Dedicated space required.
Disclaimer/Usage Instructions: Include space for this information.
4. Design Goals
Look & Feel: Simple, upmarket, and natural, with a handmade essence.
Logo Usage: Our logo is finalized and available in gold, black, and white variants. Use Josefin Bold font for the logo if adjustments are required.
Color Palette: Neutral tones (e.g., whites, blacks, golds) are preferred, with flexibility for subtle pops of color tied to each product’s main ingredient.
5. Imagery
Open to including images and colours (e.g., botanical illustrations) that highlight the main ingredient (e.g., coffee beans, turmeric root, or honeycomb). Also open to labels having a prominent colour to tie it in to the main ingredient.
Alternatively, no images can also work for a clean design.
6. Current Design Context
Our temporary design features gold leaf on top and a simple handmade side label. We’re seeking to elevate this to a more polished, cohesive design.
7. Product Line
- Body Products (Larger Jars)
Tolo Body Butter
Key Ingredients: Guarana & Cupuaçu butter (inspired by Brazil).
Note: “Tolo” is slang for “bum.”
Manuka Honey Body Butter
Key Ingredients: Manuka honey (from New Zealand) & Cupuaçu butter.
Coffee Body Scrub
Key Ingredients: Coffee and Demerara sugar.
Whipped Body Soap - Turmeric
Key Ingredients: Turmeric and Bentonite clay.
Whipped Body Soap - Banana
- Face Products (Smaller Jars)
Face Cream
Key Ingredients: Carrot Oil and Raspberry Oil.
Features natural UV protection.
Good Night Cream
Key Ingredients: Enriched with Magnesium.
Promotes relaxation and restful sleep.
8. Submission Guidelines
Flexibility: Design should allow for consistent branding across all products while accommodating the varying jar sizes and ingredient focus.
Material Considerations: Labels should complement the transparent jars and allow the product inside to remain partially visible.
Print Elements: Incorporating gold accents is a plus but should not overpower the design.
We’re excited to see your vision for a label that celebrates the natural beauty and high quality of our skincare range. Please include mockups to showcase the design in use, particularly on transparent jars of varying sizes.
women 20-50 years of age

```html
<!DOCTYPE html>
<html lang="en">
<head>
<meta charset="UTF-8">
<title>Tolo Body Butter Label</title>
<link href="https://fonts.googleapis.com/css2?family=Federo&family=Montserrat:wght@400;700&family=Josefin+Sans:wght@600&display=swap" rel="stylesheet">
<style>
  :root {
    --gold: #c4922e;
    --cream: #f6ecdc;
    --wash: #f8e4b8;
    --red: #c1162a;
    --ink: #1a1a1a;
  }
  html, body {
    margin: 0;
    padding: 0;
    width: 1200px;
    height: 600px;
    overflow: hidden;
    background: #ffffff;
  }
  .label {
    position: relative;
    width: 1200px;
    height: 600px;
    background: var(--cream);
    overflow: hidden;
    font-family: "Montserrat", sans-serif;
    color: var(--ink);
  }
  .band {
    position: absolute;
    left: 0;
    width: 100%;
    height: 22px;
    background: var(--gold);
  }
  .band--top { top: 0; }
  .band--bottom { bottom: 0; height: 23px; }

  .brand {
    position: absolute;
    top: 145px;
    left: 0;
    width: 100%;
    text-align: center;
    font-family: "Josefin Sans", sans-serif;
    font-weight: 600;
    font-size: 27px;
    letter-spacing: 5px;
    color: var(--gold);
  }
  .product-name {
    position: absolute;
    top: 196px;
    left: 0;
    width: 100%;
    margin: 0;
    text-align: center;
    font-family: "Federo", sans-serif;
    font-weight: 400;
    font-size: 68px;
    line-height: 1;
    color: var(--red);
    -webkit-text-stroke: 1.5px var(--red);
  }
  .ingredient-art {
    position: absolute;
    left: 320px;
    top: 280px;
    width: 550px;
    height: 205px;
    border-radius: 50%;
    background:
      radial-gradient(ellipse 30% 55% at 40% 55%, #d9442a 0%, rgba(217,68,42,0) 100%),
      radial-gradient(ellipse 25% 50% at 65% 55%, #e0502e 0%, rgba(224,80,46,0) 100%),
      radial-gradient(ellipse 50% 50% at 50% 50%, #5e9a3a 0%, rgba(94,154,58,0.25) 70%, rgba(94,154,58,0) 100%);
  }
  .key-ingredients {
    position: absolute;
    top: 480px;
    left: 0;
    width: 100%;
    text-align: center;
    font-size: 25px;
  }
  .volume {
    position: absolute;
    top: 522px;
    left: 0;
    width: 100%;
    text-align: center;
    font-size: 31px;
  }
  .usage {
    position: absolute;
    left: 20px;
    top: 30px;
    height: 530px;
    writing-mode: vertical-rl;
    font-size: 21.5px;
    line-height: 35px;
    margin: 0;
  }
  .ingredients {
    position: absolute;
    left: 1062px;
    top: 30px;
    height: 528px;
    writing-mode: vertical-rl;
    transform: rotate(180deg);
    font-size: 21.5px;
    line-height: 33px;
    margin: 0;
    text-align: justify;
  }
  .ingredients strong { font-weight: 700; }
</style>
</head>
<body>
  <main class="label">
    <div class="band band--top"></div>

    <p class="usage">After shower, body butter made with cupuaçu butter from amazon keeps your skin silky smooth and hydrated.</p>

    <div class="brand">MARVELLA</div>
    <h1 class="product-name">Tolo Body Butter</h1>

    <div class="ingredient-art" role="img" aria-label="Photograph of ripe red guarana fruits, one split open showing its dark seed, on fresh green leaves"></div>

    <div class="key-ingredients">Guarana &amp; Cupuaçu butter</div>
    <div class="volume">250ml</div>

    <p class="ingredients"><strong>INGREDIENTS:</strong> Shea butter, Mango butter, Cupuaçu butter, Essential Oils, Guarana infusion, and Vitamin E.</p>

    <div class="band band--bottom"></div>
  </main>
</body>
</html>
```